Texting While Driving/Distracted Driving Educational Poster

We are a design-driven nutrition, health, and wellness educational company looking for a fresh, eye-catching educational poster design to promote attentive driving, primarily to young and new drivers. Young, inexperienced drivers (under 20) have the highest proportion of distraction-related fatal crashes, with talking and texting being the most commonly recognized distraction. We hope to draw attention to this issue with an engaging, persuasive poster. The poster will be printed and available for purchase on our website and print catalogs.

Target Market(s)

The audience is American teen to adult drivers and the buyer is educators and healthcare professionals.

Requirements
Must have
• The poster must be 18" x 24" trim size, all fonts in outlines, full color art converted to CMYK.

```html
<!DOCTYPE html>
<html lang="en">
<head>
<meta charset="utf-8">
<title>Distracted Driving Poster</title>
<link rel="stylesheet" href="https://fonts.googleapis.com/css2?family=Oswald:wght@700&display=swap">
<style>
  :root {
    --page: #ffffff;
    --poster-red: #c42320;
    --red-deep: #9e1a19;
    --red-bright: #e0261f;
    --red-glow: #d9443a;
    --ink: #1b1414;
    --paper: #ffffff;
  }
  * { margin: 0; padding: 0; box-sizing: border-box; }
  html, body {
    width: 1200px;
    height: 900px;
    overflow: hidden;
    background: var(--page);
  }
  .canvas {
    position: relative;
    width: 1200px;
    height: 900px;
  }
  .poster {
    position: absolute;
    left: 288px;
    top: 34px;
    width: 624px;
    height: 832px;
    background: var(--poster-red);
    overflow: hidden;
  }
  .poster-swoosh {
    position: absolute;
    inset: 0;
    width: 100%;
    height: 100%;
  }
  .message {
    position: absolute;
    left: 0;
    right: 0;
    top: 205px;
    text-align: center;
    font-family: "Oswald", "Arial Narrow", sans-serif;
    font-weight: 700;
    font-size: 50px;
    line-height: 47.5px;
    letter-spacing: -0.5px;
    text-transform: uppercase;
  }
  .message-line { display: block; }
  .message-line--dark { color: var(--ink); }
  .message-line--light { color: var(--paper); }
</style>
</head>
<body>
<div class="canvas">
  <section class="poster" aria-label="Distracted driving awareness poster">
    <svg class="poster-swoosh" viewBox="0 0 624 832" preserveAspectRatio="none" aria-hidden="true">
      <defs>
        <radialGradient id="poster-shade" cx="50%" cy="45%" r="70%">
          <stop offset="0" stop-color="#c8261f" stop-opacity="0"/>
          <stop offset="1" stop-color="#8f1614" stop-opacity="0.35"/>
        </radialGradient>
      </defs>
      <path d="M0 55 C180 40 380 150 470 330 C540 470 560 650 624 800 L624 832 C530 690 500 500 420 360 C330 200 170 110 0 110 Z" fill="var(--red-deep)"/>
      <path d="M0 20 C200 10 400 110 500 300 C570 440 590 620 624 720 L624 760 C570 620 540 460 470 330 C380 160 190 55 0 48 Z" fill="var(--red-bright)"/>
      <path d="M60 0 C260 30 430 150 520 330 C580 450 600 560 624 620 L624 600 C590 520 570 430 520 330 C440 170 280 50 110 0 Z" fill="var(--red-glow)" opacity="0.7"/>
      <path d="M300 380 C380 480 420 640 450 832 L500 832 C470 640 430 500 360 400 Z" fill="var(--red-deep)" opacity="0.5"/>
      <rect width="624" height="832" fill="url(#poster-shade)"/>
    </svg>
    <h1 class="message">
      <span class="message-line message-line--dark">As you can see</span>
      <span class="message-line message-line--light">It’s dangerous</span>
      <span class="message-line message-line--dark">It’s not easy</span>
      <span class="message-line message-line--light">To use your phone</span>
      <span class="message-line message-line--dark">To do two things</span>
      <span class="message-line message-line--light">While you</span>
      <span class="message-line message-line--dark">At the same time.</span>
      <span class="message-line message-line--light">Are driving.</span>
    </h1>
  </section>
</div>
</body>
</html>
```